Brenmor Water - 500ml

to create a water bottle packaging similar to Brume Claire design. Bottle should be blue similar to NORTH KIND but change the design/logo to Brenmor. Wording should be similar just different design and logo. Thanks.

Colors
0054AA
0677BA
7BADD7
CADEEF
E8F1F8

Requirements
Must have
• Bottle must not be in plastic bottles. They are made in a carton instead - see NORTH KIND for reference.

```html
<!DOCTYPE html>
<html lang="en">
<head>
<meta charset="utf-8">
<title>Brenmor Water – 500ml carton options</title>
<link rel="stylesheet" href="https://fonts.googleapis.com/css2?family=Montserrat:wght@400;500;600;700;800&family=Kalam:wght@700&display=swap">
<style>
  :root {
    --white: #ffffff;
    --sky: #86bfdf;
    --body-blue: #4aade2;
    --band-light: #6cbde9;
    --deep-blue: #0a5ac2;
    --stage-top: #eceef1;
    --stage-bottom: #dcdde0;
    --footer-grey: #6b6b6b;
    --mountain-snow: #e8f1f8;
    --mountain-shade: #cadeef;
    --cap-ridge: #d3d5d9;
  }
  * { box-sizing: border-box; margin: 0; padding: 0; }
  html, body { width: 1200px; height: 598px; overflow: hidden; }
  body {
    position: relative;
    background: linear-gradient(180deg, var(--stage-top), var(--stage-bottom));
    font-family: "Montserrat", sans-serif;
  }
  .carton { position: absolute; top: 40px; width: 147px; height: 456px; }
  .carton--one { left: 398px; }
  .carton--two { left: 616px; }
  .carton__top { display: block; width: 147px; height: 79px; }
  .carton__body {
    position: relative;
    width: 147px;
    height: 377px;
    background: var(--body-blue);
    color: var(--white);
    text-align: center;
    overflow: hidden;
    border-radius: 0 0 3px 3px;
  }
  .carton__body p { line-height: 1; white-space: nowrap; }
  .carton__cap-band {
    position: absolute; left: 0; top: 0; width: 100%; height: 50px;
    background: var(--band-light);
  }
  .carton__tagline {
    position: absolute; left: 0; right: 0; top: 31px;
    font-size: 7.5px; letter-spacing: 0.9px; font-weight: 500;
  }
  .carton__brand-band {
    position: absolute; left: 0; top: 44px; width: 100%; height: 86px;
  }
  .carton__brand {
    position: absolute; left: 0; right: 0; top: 70px;
    font-size: 30px; font-weight: 800; color: var(--white); letter-spacing: -0.5px;
  }
  .carton__type {
    position: absolute; left: 0; right: 0; top: 142px;
    font-size: 9.5px; font-weight: 600; color: var(--deep-blue);
  }
  .carton__drop { position: absolute; left: 66px; top: 165px; width: 15px; height: 19px; }
  .carton__percent {
    position: absolute; left: 0; right: 0; top: 189px;
    font-size: 14px; font-weight: 700;
  }
  .carton__eco {
    position: absolute; left: 0; right: 0; top: 206px;
    font-size: 8px; letter-spacing: 0.6px; font-weight: 500;
  }
  .carton__slogan {
    position: absolute; left: 0; right: 0; top: 230px;
    font-family: "Kalam", cursive; font-weight: 700; line-height: 1;
  }
  .carton__slogan-small { display: block; font-size: 17px; }
  .carton__slogan-large { display: block; font-size: 21px; margin-top: 1px; }
  .carton__mountains {
    position: absolute; left: 0; top: 277px; width: 100%; height: 54px;
    background: linear-gradient(180deg, var(--body-blue) 0%, var(--mountain-snow) 40%, var(--mountain-shade) 75%, var(--body-blue) 100%);
  }
  .carton__volume {
    position: absolute; left: 0; right: 0; top: 338px;
    font-size: 13px; font-weight: 500;
  }
  .carton__note {
    position: absolute; left: 0; right: 0; top: 353px;
    font-size: 4.5px; font-weight: 600; letter-spacing: 0.2px;
  }
  .carton__note span { display: block; line-height: 1.4; }
  .palette-bar {
    position: absolute; left: 0; bottom: 0; width: 100%; height: 86px;
    background: var(--footer-grey);
  }
  .palette { position: absolute; top: 17px; display: flex; flex-direction: column; align-items: center; width: 160px; }
  .palette--one { left: 394px; }
  .palette--two { left: 618px; }
  .palette__swatches { display: flex; gap: 9px; }
  .swatch { width: 22px; height: 22px; }
  .swatch--white { background: var(--white); }
  .swatch--sky { background: var(--sky); }
  .swatch--body { background: var(--body-blue); }
  .swatch--deep { background: var(--deep-blue); }
  .palette__label {
    margin-top: 11px; color: var(--white);
    font-size: 13px; font-weight: 700; letter-spacing: 1.6px; line-height: 1;
  }
</style>
</head>
<body>

<svg width="0" height="0" style="position:absolute">
  <defs>
    <linearGradient id="shoulder-shade" x1="0" x2="1" y1="0" y2="0">
      <stop offset="0" stop-color="#e2e4e8"/>
      <stop offset="0.5" stop-color="#ffffff"/>
      <stop offset="1" stop-color="#e2e4e8"/>
    </linearGradient>
    <linearGradient id="cap-shade" x1="0" x2="1" y1="0" y2="0">
      <stop offset="0" stop-color="#e6e7ea"/>
      <stop offset="0.5" stop-color="#ffffff"/>
      <stop offset="1" stop-color="#e6e7ea"/>
    </linearGradient>
    <pattern id="cap-ridges" width="3.5" height="30" patternUnits="userSpaceOnUse">
      <rect width="1" height="30" fill="#c9cbcf" opacity="0.7"/>
    </pattern>
    <g id="carton-top">
      <rect x="31" y="1" width="85" height="29" rx="3" fill="url(#cap-shade)" stroke="#d2d4d8" stroke-width="0.8"/>
      <rect x="31" y="5" width="85" height="24" fill="url(#cap-ridges)"/>
      <rect x="33" y="30" width="81" height="7" fill="#f1f2f4" stroke="#d9dbde" stroke-width="0.6"/>
      <path d="M26 37 L121 37 L147 70 L147 79 L0 79 L0 70 Z" fill="url(#shoulder-shade)"/>
      <path d="M0 70 L147 70" stroke="#e0e2e6" stroke-width="0.8"/>
    </g>
  </defs>
</svg>

<article class="carton carton--one">
  <svg class="carton__top" viewBox="0 0 147 79" aria-hidden="true"><use href="#carton-top"/></svg>
  <div class="carton__body">
    <div class="carton__cap-band"></div>
    <p class="carton__tagline">PURE &amp; REFRESHING</p>
    <svg class="carton__brand-band" viewBox="0 0 147 86" preserveAspectRatio="none" aria-hidden="true">
      <path d="M0 8 Q73 -4 147 6 L147 76 Q73 62 0 74 Z" fill="var(--deep-blue)"/>
      <path d="M0 74 Q73 62 147 76 L147 81 Q73 67 0 79 Z" fill="var(--white)"/>
    </svg>
    <p class="carton__brand">Brenmor</p>
    <p class="carton__type">Natural Spring Water</p>
    <svg class="carton__drop" viewBox="0 0 14 18" aria-hidden="true">
      <path d="M7 0 C9 5 13 9 13 12 A6 6 0 0 1 1 12 C1 9 5 5 7 0 Z" fill="var(--white)"/>
      <path d="M4 12 A3 3 0 0 0 7 15" stroke="var(--body-blue)" stroke-width="1.2" fill="none"/>
    </svg>
    <p class="carton__percent">100%</p>
    <p class="carton__eco">ECO-RESPONSIBLE</p>
    <p class="carton__slogan">
      <span class="carton__slogan-small">Sourced from</span>
      <span class="carton__slogan-large">the Mountains</span>
    </p>
    <div class="carton__mountains" role="img" aria-label="Illustration of snow-capped mountains in white and pale blue"></div>
    <p class="carton__volume">500ml</p>
    <p class="carton__note"><span>SUSTAINABLY SOURCED WATER</span><span>IN A PLANT-BASED CARTON</span></p>
  </div>
</article>

<article class="carton carton--two">
  <svg class="carton__top" viewBox="0 0 147 79" aria-hidden="true"><use href="#carton-top"/></svg>
  <div class="carton__body">
    <div class="carton__cap-band"></div>
    <p class="carton__tagline">PURE &amp; REFRESHING</p>
    <svg class="carton__brand-band" viewBox="0 0 147 86" preserveAspectRatio="none" aria-hidden="true">
      <path d="M0 8 Q73 -4 147 6 L147 76 Q73 62 0 74 Z" fill="var(--deep-blue)"/>
      <path d="M0 74 Q73 62 147 76 L147 81 Q73 67 0 79 Z" fill="var(--white)"/>
    </svg>
    <p class="carton__brand">Brenmor</p>
    <p class="carton__type">Natural Spring Water</p>
    <svg class="carton__drop" viewBox="0 0 14 18" aria-hidden="true">
      <path d="M7 0 C9 5 13 9 13 12 A6 6 0 0 1 1 12 C1 9 5 5 7 0 Z" fill="var(--white)"/>
      <path d="M4 12 A3 3 0 0 0 7 15" stroke="var(--body-blue)" stroke-width="1.2" fill="none"/>
    </svg>
    <p class="carton__percent">100%</p>
    <p class="carton__eco">ECO-RESPONSIBLE</p>
    <p class="carton__slogan">
      <span class="carton__slogan-small">Sourced from</span>
      <span class="carton__slogan-large">the Mountains</span>
    </p>
    <div class="carton__mountains" role="img" aria-label="Illustration of snow-capped mountains in white and blue"></div>
    <p class="carton__volume">500ml</p>
    <p class="carton__note"><span>SUSTAINABLY SOURCED WATER</span><span>IN A PLANT-BASED CARTON</span></p>
  </div>
</article>

<footer class="palette-bar">
  <div class="palette palette--one">
    <div class="palette__swatches">
      <span class="swatch swatch--white"></span>
      <span class="swatch swatch--sky"></span>
      <span class="swatch swatch--body"></span>
      <span class="swatch swatch--deep"></span>
    </div>
    <p class="palette__label">OPTION 1</p>
  </div>
  <div class="palette palette--two">
    <div class="palette__swatches">
      <span class="swatch swatch--white"></span>
      <span class="swatch swatch--body"></span>
      <span class="swatch swatch--deep"></span>
    </div>
    <p class="palette__label">OPTION 2</p>
  </div>
</footer>

</body>
</html>
```